I need a label with logo to go on jars of honey.
Label size 70mm x 70mm
The front label should say :
The Tall Fern Honey Co. (logo)
Tarepo Honey
400g
The back label:
Would have nutritional information
And our address
You can see from the uploaded files the styles I prefer, I have uploaded a photo of the honey product too. The background of the logo doesn't have to be white. I would like to develop a color scheme that would look nice against the color of the honey.
Logo Text
The Tall Fern Honey Co. / The Tall Fern Honey Company

```html
<!DOCTYPE html>
<html lang="en">
<head>
<meta charset="utf-8">
<title>The Tall Fern Honey Co. – Tarepo Honey labels</title>
<link href="https://fonts.googleapis.com/css2?family=Oswald:wght@500;600&display=swap" rel="stylesheet">
<style>
  :root {
    --page: #ffffff;
    --green-deep: #0b2f1c;
    --green-mid: #1e4d33;
    --green-sheen: #3d6b52;
    --gold: #e2b514;
    --gold-light: #f6dc86;
    --gold-dark: #9c6a1c;
    --silver: #f4f3ef;
    --silver-shade: #cfcbc1;
    --ink-green: #1c4327;
    --ink-dark: #2a2a2a;
    --cream: #f3dd9a;
  }
  html, body {
    margin: 0;
    width: 1200px;
    height: 830px;
    overflow: hidden;
    background: var(--page);
  }
  .label-sheet {
    display: block;
    width: 1200px;
    height: 830px;
  }
  .brand-name {
    font-family: "Oswald", sans-serif;
    font-weight: 600;
    fill: var(--gold);
  }
  .product-name {
    font-family: "Oswald", sans-serif;
    font-weight: 600;
    fill: var(--ink-green);
  }
  .net-weight {
    font-family: "Oswald", sans-serif;
    font-weight: 500;
    font-size: 19px;
  }
  .net-weight--dark { fill: var(--ink-dark); }
  .net-weight--gold { fill: var(--gold); }
  .star--cream { fill: var(--cream); }
  .star--gold { fill: var(--gold); }
  .brand-mark { fill: var(--gold); }
</style>
</head>
<body>
<svg class="label-sheet" viewBox="0 0 1200 830" xmlns="http://www.w3.org/2000/svg">
  <defs>
    <linearGradient id="gold-frame" x1="0" y1="0" x2="1" y2="1">
      <stop offset="0" stop-color="#f6dc86"/>
      <stop offset="0.35" stop-color="#b9852a"/>
      <stop offset="0.6" stop-color="#f3d27a"/>
      <stop offset="1" stop-color="#9c6a1c"/>
    </linearGradient>
    <linearGradient id="green-field" x1="0" y1="0" x2="1" y2="0">
      <stop offset="0" stop-color="#0b2f1c"/>
      <stop offset="0.3" stop-color="#0f3a24"/>
      <stop offset="0.55" stop-color="#082a18"/>
      <stop offset="0.85" stop-color="#3d6b52"/>
      <stop offset="1" stop-color="#0b2f1c"/>
    </linearGradient>
    <linearGradient id="silver-band" x1="0" y1="0" x2="1" y2="0">
      <stop offset="0" stop-color="#cfcbc1"/>
      <stop offset="0.3" stop-color="#f7f6f2"/>
      <stop offset="0.6" stop-color="#e6e3dc"/>
      <stop offset="0.85" stop-color="#ffffff"/>
      <stop offset="1" stop-color="#c9c5bb"/>
    </linearGradient>
    <radialGradient id="honey-tone" cx="0.5" cy="0.55" r="0.6">
      <stop offset="0" stop-color="#f7c531"/>
      <stop offset="0.7" stop-color="#e9a923"/>
      <stop offset="1" stop-color="#f4e6c8"/>
    </radialGradient>
    <path id="arched-shape" d="M78,190 C120,110 220,88 298,88 C376,88 476,110 520,190 L520,205 Q530,215 545,215 L555,215 L555,640 L545,640 Q530,640 520,655 L520,665 C470,725 380,745 298,745 C216,745 126,725 78,665 L78,655 Q66,640 52,640 L42,640 L42,215 L52,215 Q66,215 78,205 Z"/>
    <path id="notched-shape" d="M660,110 L1105,110 Q1110,140 1142,148 L1142,685 Q1110,690 1105,722 L660,722 Q655,690 622,685 L622,148 Q655,140 660,110 Z"/>
    <clipPath id="arched-inner-clip">
      <use href="#arched-shape" transform="translate(298.5 416.5) scale(0.955 0.965) translate(-298.5 -416.5)"/>
    </clipPath>
    <polygon id="star" points="0,-11 3.2,-3.5 11,-3.4 4.9,1.6 7,9.5 0,5 -7,9.5 -4.9,1.6 -11,-3.4 -3.2,-3.5"/>
  </defs>

  <!-- Arched label -->
  <g class="label label--arched">
    <use href="#arched-shape" fill="url(#gold-frame)"/>
    <g clip-path="url(#arched-inner-clip)">
      <rect x="40" y="80" width="520" height="670" fill="url(#green-field)"/>
      <rect x="40" y="518" width="520" height="230" fill="url(#silver-band)"/>
      <rect x="40" y="600" width="520" height="2" fill="var(--silver-shade)"/>
    </g>

    <g class="stars stars--top">
      <use href="#star" class="star--cream" x="217" y="152"/>
      <use href="#star" class="star--cream" x="257" y="135"/>
      <use href="#star" class="star--cream" x="298" y="128"/>
      <use href="#star" class="star--cream" x="340" y="135"/>
      <use href="#star" class="star--cream" x="381" y="152"/>
    </g>

    <circle class="brand-mark" cx="300" cy="258" r="62"/>

    <text class="brand-name" x="298" y="478" font-size="54" text-anchor="middle" textLength="410" lengthAdjust="spacingAndGlyphs">THE TALL FERN HONEY CO.</text>
    <text class="product-name" x="298" y="582" font-size="54" text-anchor="middle" textLength="320" lengthAdjust="spacingAndGlyphs">TAREPO HONEY</text>

    <rect role="img" aria-label="Decorative scroll flourish" x="236" y="598" width="126" height="16" rx="8" fill="#5f6d63" opacity="0.55"/>

    <text class="net-weight net-weight--dark" x="298" y="663" text-anchor="middle">400G</text>

    <g class="stars stars--bottom">
      <use href="#star" class="star--gold" x="217" y="678"/>
      <use href="#star" class="star--gold" x="257" y="692"/>
      <use href="#star" class="star--gold" x="298" y="700"/>
      <use href="#star" class="star--gold" x="340" y="692"/>
      <use href="#star" class="star--gold" x="381" y="678"/>
    </g>
  </g>

  <!-- Notched label -->
  <g class="label label--notched">
    <use href="#notched-shape" fill="#111"/>
    <use href="#notched-shape" fill="url(#gold-frame)" transform="translate(882 416) scale(0.99 0.99) translate(-882 -416)"/>
    <use href="#notched-shape" fill="url(#green-field)" transform="translate(882 416) scale(0.965 0.97) translate(-882 -416)"/>

    <circle class="brand-mark" cx="882" cy="220" r="46"/>

    <text class="brand-name" x="882" y="345" font-size="58" text-anchor="middle" textLength="410" lengthAdjust="spacingAndGlyphs">THE TALL FERN HONEY CO.</text>

    <rect x="639" y="362" width="487" height="203" fill="url(#gold-frame)"/>
    <rect x="642" y="365" width="481" height="197" fill="url(#silver-band)"/>

    <text class="product-name" x="882" y="443" font-size="62" text-anchor="middle" textLength="325" lengthAdjust="spacingAndGlyphs">TAREPO HONEY</text>

    <rect role="img" aria-label="Sketch of a honey pot with dipper and daisies" x="822" y="458" width="130" height="98" rx="30" fill="url(#honey-tone)"/>

    <rect role="img" aria-label="Decorative scroll flourish" x="818" y="580" width="128" height="16" rx="8" fill="var(--gold-light)" opacity="0.6"/>

    <text class="net-weight net-weight--gold" x="882" y="690" text-anchor="middle">400G</text>
  </g>
</svg>
</body>
</html>
```